【 概要 】 ペットアレルギー検査キット「ソヨナビ」の広告施策として DM(ダイレクトメール)実施に伴い、配布するチラシ制作を募集します。 下記がLPになります。 https://kirune-works.jp/lp/dc_allergy/ LPの素材などは全てお渡し可能です。 【 依頼内容 】 ・サイズ:A4 両面 ・ページ数:2ページ(裏表) ・素材の用意(画像):こちらで用意します。(CVRが高くなる提案などいただけると有り難いです) ・デザイン内容:表には主に「商品の特徴/性質」、裏には「検査結果(今までの実績の声)」などを掲載予定ですが、ご提案いただくことも可能です。 【 デザインイメージ 】 ・ターゲット層:ペットを飼っている方(定価¥32,670-のため、それを購入してくださるユーザー) ・雰囲気:購買への動機付けになるのであれば何でもいいです。高価格帯ではなるので多少の権威性/安心などの要素はほしいです。 【 契約金額(税抜) 】 5万円 ※契約金額(税込)からシステム利用料を差し引いた金額が、ワーカーさまの受取金額となります その他ご質問等ありましたら、気軽にお問い合わせください。 ご応募をお待ちしております! |
| https://kirune-works.jp/lp/dc_allergy/ | ||
多くの案いただきまして、どの案も素晴らしかったです。
事業部全体の投票の結果、こちらの提案を採用いたします。
皆様、ご提案、誠にありがとうございました。どの提案も素晴らしく非常にありがたく、選ぶことが大変困難でした。また機会がありましたらよろしくお願いいたします。

```html
<!DOCTYPE html>
<html lang="ja">
<head>
<meta charset="utf-8">
<title>ソヨナビ ペット用アレルギー不耐性テストキット</title>
<link rel="stylesheet" href="https://fonts.googleapis.com/css2?family=Noto+Sans+JP:wght@500;700;900&display=swap">
<style>
  :root {
    --teal: #15a3a6;
    --teal-deep: #0b8b93;
    --green: #4fc39a;
    --ink: #333333;
    --paper: #f6f7f7;
    --white: #ffffff;
    --yellow: #fff45c;
    --tick: #e2473b;
    --photo-warm: #e9d3b4;
    --photo-light: #f3ece2;
    --box-blue: #cfe9ee;
    --medal: #c9a445;
    --shield: #2f6f9a;
  }
  * { margin: 0; padding: 0; box-sizing: border-box; }
  html, body { width: 848px; height: 1200px; overflow: hidden; }
  body {
    font-family: "Noto Sans JP", sans-serif;
    color: var(--ink);
    background: var(--paper);
    position: relative;
  }
  .flyer { position: relative; width: 848px; height: 1200px; overflow: hidden; }

  /* Top: headline */
  .lead {
    position: absolute; top: 20px; left: 0; width: 100%;
    text-align: center; color: var(--teal-deep);
    font-weight: 700; font-size: 32px; line-height: 44px; white-space: nowrap;
  }
  .headline-band {
    position: absolute; top: 76px; left: 114px; width: 620px; height: 84px;
    background: var(--teal); border-radius: 4px;
    display: flex; align-items: center; justify-content: center;
    color: var(--white); font-weight: 900; font-size: 60px; line-height: 1;
    white-space: nowrap;
  }
  .headline-tail {
    position: absolute; top: 166px; left: 0; width: 100%;
    text-align: center; color: var(--teal-deep);
    font-weight: 900; font-size: 38px; line-height: 48px;
  }

  /* Photo */
  .hero-photo {
    position: absolute; top: 222px; left: 0; width: 848px; height: 358px;
    background: linear-gradient(100deg, var(--photo-light) 0%, var(--photo-warm) 45%, var(--photo-light) 100%);
  }

  /* Speech bubble */
  .bubble {
    position: absolute; top: 240px; left: 500px; width: 330px; height: 170px;
    background: var(--white); border: 4px solid var(--teal);
    border-radius: 80px;
    display: flex; align-items: center; justify-content: center;
    text-align: center; font-weight: 900; font-size: 28px; line-height: 1.4;
    color: var(--ink);
  }
  .bubble em { font-style: normal; color: var(--tick); }
  .bubble-tail { position: absolute; top: 395px; left: 560px; }

  /* Symptom checklist */
  .symptoms {
    position: absolute; top: 432px; left: 50px; width: 680px; height: 128px;
    background: var(--white); border-radius: 6px;
    box-shadow: 0 3px 10px rgba(0,0,0,0.12);
    display: grid; grid-template-columns: 1fr 1fr; align-content: center;
    row-gap: 20px; column-gap: 16px; padding: 0 22px; list-style: none;
  }
  .symptom { display: flex; align-items: center; gap: 10px; font-weight: 700; font-size: 21px; white-space: nowrap; }
  .symptom svg { flex: none; }

  /* Solution section */
  .solution {
    position: absolute; top: 590px; left: 0; width: 848px; height: 610px;
    background: linear-gradient(180deg, var(--teal) 0%, var(--teal-deep) 55%, var(--green) 100%);
  }
  .solution-lead {
    position: absolute; top: 30px; left: 0; width: 100%;
    text-align: center; color: var(--white); font-weight: 700; font-size: 23px; white-space: nowrap;
  }
  .brand-chip {
    display: inline-block; background: var(--white); color: var(--teal-deep);
    font-weight: 900; padding: 0 10px; border-radius: 4px; margin: 0 4px;
  }
  .divider { position: absolute; top: 84px; left: 36px; width: 776px; height: 2px; background: rgba(255,255,255,0.5); }

  .method { position: absolute; top: 112px; left: 36px; color: var(--white); font-weight: 700; font-size: 18px; white-space: nowrap; }
  .product-name { position: absolute; top: 150px; left: 36px; display: flex; align-items: flex-end; gap: 8px; color: var(--white); }
  .product-name .brand-plate {
    background: var(--white); color: var(--teal-deep); font-weight: 900;
    font-size: 60px; line-height: 1; padding: 8px 14px; border-radius: 6px;
  }
  .product-name .particle { font-weight: 900; font-size: 34px; line-height: 1.2; }
  .kit-title { position: absolute; top: 250px; left: 36px; color: var(--white); font-weight: 900; line-height: 1.25; white-space: nowrap; }
  .kit-title .small { font-size: 28px; display: block; }
  .kit-title .big { font-size: 40px; display: block; }

  .promise { position: absolute; top: 470px; left: 36px; color: var(--yellow); font-weight: 900; font-size: 30px; line-height: 1.4; white-space: nowrap; }

  .product-photo {
    position: absolute; top: 110px; left: 400px; width: 420px; height: 300px;
    background: linear-gradient(160deg, var(--white) 0%, var(--box-blue) 100%);
    border-radius: 6px; box-shadow: 0 6px 14px rgba(0,0,0,0.2);
  }

  .trust-shield { position: absolute; top: 460px; left: 548px; }

  .awards { position: absolute; top: 480px; left: 630px; display: flex; gap: 10px; }
  .award { width: 56px; height: 56px; border-radius: 50%; background: var(--medal); border: 3px solid var(--white); }
</style>
</head>
<body>
<div class="flyer">
  <p class="lead">調子が悪いそのサイン、病気ではなく</p>
  <h1 class="headline-band">アレルギー・不耐性</h1>
  <p class="headline-tail">が原因かも?</p>

  <div class="hero-photo" role="img" aria-label="子猫と子犬が寄り添って眠っている写真"></div>

  <div class="bubble"><p>愛犬・愛猫に<br><em>このような症状</em>は<br>ありませんか?</p></div>
  <svg class="bubble-tail" width="40" height="40" viewBox="0 0 40 40" aria-hidden="true">
    <path d="M4 0 L36 0 L8 36 Z" fill="#ffffff" stroke="#15a3a6" stroke-width="4" stroke-linejoin="round"/>
    <rect x="2" y="-4" width="36" height="6" fill="#ffffff"/>
  </svg>

  <ul class="symptoms">
    <li class="symptom"><svg width="26" height="26" viewBox="0 0 26 26"><rect x="1" y="3" width="22" height="22" fill="none" stroke="#333" stroke-width="2"/><path d="M5 13 L11 19 L24 3" fill="none" stroke="#e2473b" stroke-width="4" stroke-linecap="round"/></svg>痒み、赤みがおさまらない</li>
    <li class="symptom"><svg width="26" height="26" viewBox="0 0 26 26"><rect x="1" y="3" width="22" height="22" fill="none" stroke="#333" stroke-width="2"/><path d="M5 13 L11 19 L24 3" fill="none" stroke="#e2473b" stroke-width="4" stroke-linecap="round"/></svg>咳、鼻水、目やにが出る</li>
    <li class="symptom"><svg width="26" height="26" viewBox="0 0 26 26"><rect x="1" y="3" width="22" height="22" fill="none" stroke="#333" stroke-width="2"/><path d="M5 13 L11 19 L24 3" fill="none" stroke="#e2473b" stroke-width="4" stroke-linecap="round"/></svg>軟便、下痢が続いてる</li>
    <li class="symptom"><svg width="26" height="26" viewBox="0 0 26 26"><rect x="1" y="3" width="22" height="22" fill="none" stroke="#333" stroke-width="2"/><path d="M5 13 L11 19 L24 3" fill="none" stroke="#e2473b" stroke-width="4" stroke-linecap="round"/></svg>涙やけが止まらない</li>
  </ul>

  <section class="solution">
    <p class="solution-lead">アレルギー・不耐性のお悩みは、<span class="brand-chip">ソヨナビ</span>がすべて解決</p>
    <div class="divider"></div>

    <p class="method">ペットの被毛によるバイオレゾナンス検査</p>
    <div class="product-name"><span class="brand-plate">ソヨナビ</span><span class="particle">の</span></div>
    <h2 class="kit-title"><span class="small">ペット用</span><span class="big">アレルギー不耐性</span><span class="big">テストキット</span></h2>

    <p class="promise">痛くない!怖くない!<br>ご自宅から体毛を送るだけ!!</p>

    <div class="product-photo" role="img" aria-label="犬猫用不耐性検査キットのパッケージ写真"></div>

    <svg class="trust-shield" width="66" height="80" viewBox="0 0 90 110" aria-hidden="true">
      <path d="M45 4 L84 18 L84 54 C84 80 66 98 45 106 C24 98 6 80 6 54 L6 18 Z" fill="#2f6f9a" stroke="#ffffff" stroke-width="4"/>
    </svg>

    <div class="awards">
      <div class="award"></div>
      <div class="award"></div>
      <div class="award"></div>
    </div>
  </section>
</div>
</body>
</html>
```